Vel Techniqos Logo Design

We need a business card design for Las Vegas based company called "Vel Techniqs" (http://www.veltechniqs-example.com). Vel Techniqs prides itself in providing in-depth knowledge that is based on real-world experience in the field of wireless telecommunications. Our practice covers strategy, marketing, and business development across the entire telecom value chain – from consumer to enterprise, content to applications, and mobile devices to wireless infrastructure. Our expertise is in the fields of wireless telecommunications, network optimization, specializing in CDMA, UMTS, WiMAX and LTE solutions.
The logo attached could be reused for the business card, but would prefer a new innovative logo as well. The final design should project cutting edge wireless technologies. The design should also communicate a modern business that has expertise and is focused on R&D.
Updates

Team,

  Forgot to mention this.  While Vel Techniqs is focused in wireless technologies, the word 'Vel' comes from Hindi language and means harmonious music

Project Deadline Extended
Reason: Extending deadline to allow for the designer to complete final changes. Thank you all for submitting the designs so far. Thanks, Rohan.

Industry/Entity Type

Business

Logo Text

Vel Techniqs

```html
<!DOCTYPE html>
<html lang="en">
<head>
<meta charset="utf-8">
<title>Vel Techniqos Logo Design</title>
<link rel="stylesheet" href="https://fonts.googleapis.com/css2?family=Arimo:wght@400;700&family=Questrial&display=swap">
<style>
  :root {
    --page-bg: #f3f3f3;
    --page-bg-edge: #e4e4e4;
    --band: #000000;
    --caption: #ffffff;
    --front-bg: #ffffff;
    --front-shard-light: #f4f5f6;
    --front-shard-mid: #d9dcdf;
    --brand-blue: #1f86d6;
    --brand-mark: #2a95e8;
    --back-bg-deep: #0b1e2c;
    --back-bg-mid: #12344a;
    --back-shard: #1d5474;
    --text-white: #ffffff;
    --text-soft: #c8d4de;
    --accent-cyan: #2ad0ef;
    --mark-light: #5bb8f2;
  }
  * { margin: 0; padding: 0; box-sizing: border-box; }
  html, body { width: 1200px; height: 848px; overflow: hidden; }
  body {
    position: relative;
    font-family: "Arimo", Arial, sans-serif;
    background: radial-gradient(ellipse at 50% 40%, var(--page-bg) 0%, var(--page-bg) 55%, var(--page-bg-edge) 100%);
  }
  .corner-band { position: absolute; left: 0; top: 0; }
  .card {
    position: absolute;
    width: 587px;
    height: 352px;
    border-radius: 14px;
    overflow: hidden;
    box-shadow: 0 4px 10px rgba(0,0,0,0.25);
  }
  .card-front { left: 97px; top: 111px; background: var(--front-bg); }
  .card-back { left: 514px; top: 362px; background: var(--back-bg-deep); }
  .card-art { position: absolute; inset: 0; }
  .card-front .card-art {
    background:
      linear-gradient(160deg, transparent 0%, transparent 45%, var(--front-shard-light) 60%, var(--front-shard-mid) 75%, var(--front-shard-light) 100%),
      linear-gradient(20deg, var(--front-shard-mid) 0%, var(--front-shard-light) 25%, transparent 40%);
  }
  .card-back .card-art {
    background:
      radial-gradient(ellipse at 30% 30%, var(--back-bg-mid) 0%, transparent 60%),
      linear-gradient(200deg, var(--back-shard) 0%, transparent 35%),
      linear-gradient(20deg, var(--back-shard) 0%, transparent 40%),
      var(--back-bg-deep);
  }
  .brand-mark { position: absolute; border-radius: 50%; background: var(--brand-mark); }
  .card-front .brand-mark { left: 226px; top: 69px; width: 144px; height: 144px; }
  .card-back .brand-mark { left: 437px; top: 215px; width: 61px; height: 61px; background: var(--mark-light); }
  .brand-name {
    position: absolute;
    font-weight: 400;
    text-transform: uppercase;
    white-space: nowrap;
    transform: translateX(-50%);
  }
  .card-front .brand-name {
    left: 294px; top: 222px;
    font-size: 34px; letter-spacing: 3px;
    color: var(--brand-blue);
  }
  .card-back .brand-name {
    left: 467px; top: 282px;
    font-size: 16px; letter-spacing: 1.5px;
    color: var(--mark-light);
  }
  .person { position: absolute; left: 40px; top: 56px; }
  .person-name { font-size: 28px; color: var(--text-white); line-height: 32px; }
  .person-title { font-size: 15px; color: var(--text-soft); line-height: 18px; }
  .company { position: absolute; left: 40px; top: 130px; }
  .company-name { font-size: 15px; color: var(--accent-cyan); line-height: 18px; margin-bottom: 4px; }
  .company-address { font-size: 11px; color: var(--text-soft); line-height: 14px; font-style: normal; }
  .contact { position: absolute; left: 307px; top: 89px; list-style: none; }
  .contact li { font-size: 13.5px; color: var(--text-white); line-height: 24px; }
  .contact .web { color: var(--accent-cyan); font-style: italic; }
  .footer-bar {
    position: absolute; left: 0; bottom: 0;
    width: 1200px; height: 55px;
    background: var(--band);
  }
  .footer-caption {
    position: absolute; left: 62px; top: 17px;
    font-family: "Questrial", Arial, sans-serif;
    font-size: 16px; color: var(--caption);
  }
</style>
</head>
<body>
  <svg class="corner-band" width="230" height="110" viewBox="0 0 230 110" aria-hidden="true">
    <polygon points="0,48 152,0 226,0 0,102" fill="var(--band)"/>
  </svg>

  <section class="card card-front">
    <div class="card-art" role="img" aria-label="Pale grey crystal shard illustration"></div>
    <div class="brand-mark"></div>
    <div class="brand-name">Vel Techniqs</div>
  </section>

  <section class="card card-back">
    <div class="card-art" role="img" aria-label="Dark blue crystal shard illustration"></div>
    <div class="person">
      <div class="person-name">Rohan Mehta</div>
      <div class="person-title">Executive Director</div>
    </div>
    <div class="company">
      <div class="company-name">Vel Techniqs</div>
      <address class="company-address">36 Larkspur Ridge Way,<br>Unit 14B,<br>Marlow Falls, OR 97000</address>
    </div>
    <ul class="contact">
      <li>Ph: +1 555-010-2946</li>
      <li>Email: rohan@veltechniqs-example.com</li>
      <li>Website: <span class="web">www.veltechniqs-example.com</span></li>
    </ul>
    <div class="brand-mark"></div>
    <div class="brand-name">Vel Techniqs</div>
  </section>

  <footer class="footer-bar">
    <div class="footer-caption">Vel Techniqos Logo Design</div>
  </footer>
</body>
</html>
```